Velvet Crypt Mixtape Podcast Design

My audio drama podcast is a funny horror story with romantic elements called Velvet Crypt Mixtape.
I'm looking for a colorful design featuring the title and letting the viewer know this is a horror show.
The title needs to be clearly visible even in thumbnail size.

```html
<!DOCTYPE html>
<html lang="en">
<head>
<meta charset="utf-8">
<title>Velvet Crypt Mixtape Podcast</title>
<link rel="stylesheet" href="https://fonts.googleapis.com/css2?family=Marcellus&family=Sacramento&display=swap">
<style>
  :root {
    --sky-glow: #f0a3ad;
    --sky-mid: #d0323f;
    --sky-deep: #7a0c14;
    --sky-edge: #2a0406;
    --ground: #0d0203;
    --title: #ffd9de;
    --title-glow: rgba(255, 90, 120, 0.85);
    --neon: #ff7ec6;
    --neon-glow: rgba(255, 60, 170, 0.9);
    --moon: #fbf4f4;
  }
  * { margin: 0; padding: 0; box-sizing: border-box; }
  html, body {
    width: 1200px;
    height: 1200px;
    overflow: hidden;
    background: var(--ground);
  }
  .cover {
    position: relative;
    width: 1200px;
    height: 1200px;
    overflow: hidden;
  }
  .scene {
    position: absolute;
    inset: 0;
    background:
      linear-gradient(to bottom, rgba(0,0,0,0) 0%, rgba(0,0,0,0) 58%, rgba(13,2,3,0.85) 80%, var(--ground) 100%),
      radial-gradient(ellipse 55% 40% at 52% 55%, var(--sky-glow) 0%, var(--sky-mid) 45%, var(--sky-deep) 75%, var(--sky-edge) 100%);
  }
  .moon {
    position: absolute;
    left: 563px;
    top: 51px;
    width: 74px;
    height: 74px;
    border-radius: 50%;
    background: var(--moon);
    box-shadow: 0 0 22px rgba(255, 220, 225, 0.8);
  }
  .title {
    position: absolute;
    left: 0;
    right: 0;
    top: 170px;
    text-align: center;
    font-family: "Marcellus", serif;
    font-weight: 400;
    color: var(--title);
    font-size: 176px;
    line-height: 166px;
    letter-spacing: 2px;
    text-transform: uppercase;
    text-shadow: 0 0 14px var(--title-glow), 0 0 34px var(--title-glow);
  }
  .title span { display: block; }
  .label {
    position: absolute;
    left: 735px;
    top: 975px;
    font-family: "Sacramento", cursive;
    font-size: 118px;
    line-height: 1;
    color: var(--neon);
    text-shadow: 0 0 8px var(--neon-glow), 0 0 22px var(--neon-glow);
  }
</style>
</head>
<body>
  <main class="cover">
    <div class="scene" role="img" aria-label="Blood-red cloudy sky over a dark plain with bare trees at the edges and four silhouetted figures walking away toward the horizon"></div>
    <div class="moon" aria-hidden="true"></div>
    <h1 class="title">
      <span>Velvet</span>
      <span>Crypt</span>
      <span>Mixtape!</span>
    </h1>
    <p class="label">Podcast</p>
  </main>
</body>
</html>
```